Consumer Product Goods (Food) website

We need a simple, but clean and modern website for our new food branded company called Lantern Bay Foods.

Need a website that company can easily update. I added company logo and some images of our products. I added 1 package design of our products that's available now in the retail stores.

Company currently has 1 item but will be adding up to 5 items witin a few months. So need a website we can easily add new products.

Reason: We're guaranteeing payment and wanted to give more time for others to submit.

Target Market(s)

Customers that are seeking new adventurous novelty Asian foods.

Industry/Entity Type

Retail

Coding

Coded - Design and coding required

Number of Pages Required

3 page

Requirements
Must have
• I would like to have 3 pages: Homepage, Products Page, and Contact Us.
Nice to have
• I would like a nice visually clean and modern looking homepage. As you can see from the package design, it has a dark tone, so if we can try to make the website a dark blackgroup. I uploaded the dark background we used in our package. Maybe have the 3 different dumplings rotating images on the homepage.
• Products Page should have just 1 product right now; Kimchi & Pork dumplings. Maybe have like pic of the package design and have space for a briefly summary of product, ingredient list and nutrition fact. Should be a page where i can add more products to this page.
• Contact Us page can simply have map, email addres, and phone #.
• would be nice to have where the website is responsive to PC, tablet, and mobile phones

```html
<!DOCTYPE html>
<html lang="en">
<head>
<meta charset="utf-8">
<title>Lantern Bay Foods</title>
<link rel="stylesheet" href="https://fonts.googleapis.com/css2?family=Jost:wght@300;400;500&family=Lato:ital,wght@0,400;0,700;1,400&display=swap">
<style>
:root{
  --green:#7fc72a;
  --green-dark:#6aad1e;
  --wood:#2b2825;
  --wood-dark:#1f1d1b;
  --wood-deep:#161514;
  --ink:#222;
  --white:#fff;
  --muted:#d8d8d8;
}
*{box-sizing:border-box;margin:0;padding:0}
html,body{width:1200px;height:2406px;overflow:hidden}
body{
  background:linear-gradient(90deg,#3a3733 0%,#2a2826 50%,#3a3733 100%);
  font-family:'Lato',sans-serif;color:var(--white);position:relative;
}
.page{position:absolute;left:90px;top:0;width:1020px;height:2406px;background:var(--wood)}
.abs{position:absolute}

/* top bar */
.topbar{left:0;top:0;width:1020px;height:42px;background:var(--green)}
.topbar .contact{position:absolute;right:16px;top:10px;display:flex;gap:22px;font-size:15px}
.topbar .contact span{display:flex;align-items:center;gap:7px}

/* hero */
.hero{left:0;top:42px;width:1020px;height:545px;
  background:radial-gradient(ellipse at 55% 50%,#d9d3c6 0%,#8d8678 30%,#3c3834 60%,#1e1c1a 100%)}
.brand{position:absolute;left:10px;top:62px;display:flex;align-items:center;gap:10px;
  font-family:'Jost',sans-serif;font-weight:500;font-size:30px;color:var(--white);letter-spacing:.5px}
.brand .mark{width:34px;height:34px;background:var(--green);border-radius:6px}
.nav{position:absolute;top:45px;left:450px;display:flex;font-family:'Jost',sans-serif;font-size:15px}
.nav a{color:var(--white);text-decoration:none;position:absolute;white-space:nowrap}
.nav a.active{color:var(--green)}
.search{position:absolute;left:993px;top:46px}
.hero h1{position:absolute;top:315px;width:100%;text-align:center;font-family:'Jost',sans-serif;font-weight:300;font-size:36px;letter-spacing:.5px}
.hero p{position:absolute;top:370px;width:100%;text-align:center;font-family:'Jost',sans-serif;font-size:17px;letter-spacing:.3px}
.arrow{position:absolute;width:34px;height:34px;border-radius:50%;background:rgba(255,255,255,.85);display:flex;align-items:center;justify-content:center}
.green-rule{left:0;top:587px;width:1020px;height:4px;background:var(--green)}

/* sections */
.section-title{position:absolute;width:100%;text-align:center;font-family:'Jost',sans-serif;font-weight:400;font-size:35px;letter-spacing:.5px}
.section-title em{font-style:normal;color:var(--green)}
.divider{position:absolute;height:12px}
.divider::before,.divider::after{content:"";position:absolute;top:6px;height:1px;width:calc(50% - 14px);background:#cfcfcf}
.divider::before{left:0}.divider::after{right:0}
.divider i{position:absolute;left:50%;top:2px;width:10px;height:8px;margin-left:-5px;border:1px solid #cfcfcf;border-top:none;border-radius:0 0 6px 6px}
.btn{position:absolute;font-family:'Lato',sans-serif;font-weight:700;font-size:13px;display:flex;align-items:center;justify-content:center;border-radius:3px;color:var(--white)}

.about{left:0;top:591px;width:1020px;height:328px;background:linear-gradient(180deg,#2a2724,#34302c 60%,#2a2724)}
.about .copy{position:absolute;left:55px;top:148px;width:910px;text-align:center;font-size:13px;line-height:23px;color:#eee}
.about .btn{left:459px;top:248px;width:102px;height:29px;background:var(--green)}

.products{left:0;top:919px;width:1020px;height:654px;background:var(--wood-dark)}
.product-photo{position:absolute;left:0;top:144px;width:503px;height:510px;
  background:radial-gradient(ellipse at 45% 55%,#ece6d8 0%,#c9c2b0 35%,#7d8a8c 70%,#2a3438 100%)}
.product-panel{position:absolute;left:503px;top:144px;width:517px;height:510px;background:var(--green)}
.product-panel h3{position:absolute;left:42px;top:56px;font-family:'Jost',sans-serif;font-weight:500;font-size:25px;color:var(--ink)}
.product-panel .lead{position:absolute;left:42px;top:97px;font-family:'Jost',sans-serif;font-size:17px;color:var(--white)}
.product-panel h4{position:absolute;left:42px;font-family:'Jost',sans-serif;font-weight:500;font-size:16px;color:var(--white);display:flex;align-items:center;gap:12px;letter-spacing:.3px}
.product-panel .text{position:absolute;left:42px;width:440px;font-size:12.5px;line-height:23px;color:var(--white)}
.product-panel .btn{left:44px;top:392px;width:104px;height:32px;background:var(--ink)}

.testimonials{left:0;top:1573px;width:1020px;height:411px;background:linear-gradient(180deg,#2b2825,#2f2b28 50%,#252321)}
.quote{position:absolute;left:70px;top:136px;width:880px;text-align:center;font-style:italic;font-size:14px;line-height:24px;color:#eee}
.client-name{position:absolute;left:0;top:220px;width:100%;display:flex;justify-content:center;align-items:center;gap:10px;font-family:'Jost',sans-serif;font-weight:500;font-size:20px;color:var(--green)}
.avatar{position:absolute;border-radius:50%;background:radial-gradient(circle at 50% 40%,#b79a84,#5e4a3e);border:3px solid #ddd}
.avatar.current{border:4px solid var(--green)}

.newsletter{left:0;top:1984px;width:1020px;height:108px;background:var(--green)}
.newsletter .icon{position:absolute;left:10px;top:36px;width:40px;height:40px;border-radius:50%;background:var(--ink);border:2px solid var(--white);display:flex;align-items:center;justify-content:center}
.newsletter h2{position:absolute;left:74px;top:33px;font-family:'Jost',sans-serif;font-weight:400;font-size:33px}
.newsletter .field{position:absolute;left:393px;top:35px;width:473px;height:39px;background:var(--white);color:#777;font-size:12.5px;padding:12px 16px}
.newsletter .btn{left:908px;top:39px;width:102px;height:30px;background:var(--ink);font-size:14px;letter-spacing:.3px}

.footer{left:0;top:2092px;width:1020px;height:271px;background:linear-gradient(120deg,#1b1a18 0%,#2c2925 45%,#3a332b 70%,#22201d 100%)}
.footer h5{position:absolute;top:40px;font-family:'Lato',sans-serif;font-weight:700;font-size:15px}
.footer ul{list-style:none;position:absolute;left:8px;top:80px}
.footer li{font-size:13px;height:45px;display:flex;gap:9px}
.footer .line{position:absolute;left:180px;display:flex;gap:12px;font-size:13px;line-height:18px}
.map{position:absolute;left:491px;top:80px;width:269px;height:151px;background:linear-gradient(135deg,#e7e4df,#d4d0c8)}
.footer-brand{position:absolute;left:840px;top:140px;display:flex;align-items:center;gap:8px;font-family:'Jost',sans-serif;font-weight:500;font-size:24px;color:#e8e8e8}
.footer-brand .mark{width:26px;height:26px;border-radius:50%;background:#e8e8e8}
.bottom{left:0;top:2363px;width:1020px;height:43px;background:#111}
.bottom p{position:absolute;left:8px;top:14px;font-size:11.5px}
.social{position:absolute;top:12px;width:20px;height:20px;border-radius:50%;border:1px solid #ccc}
</style>
</head>
<body>
<div class="page">

  <header class="abs topbar">
    <div class="contact">
      <span><svg width="16" height="16" viewBox="0 0 16 16"><circle cx="8" cy="8" r="7" fill="none" stroke="#fff" stroke-width="1.4"/><path d="M5.5 4.5l1.5 1.5-1 1c.6 1.2 1.3 1.9 2.5 2.5l1-1 1.5 1.5-1 1c-2.5-.4-4.6-2.5-5-5z" fill="#fff"/></svg>555 010 2468</span>
      <span><svg width="18" height="12" viewBox="0 0 18 12"><rect x="0.5" y="0.5" width="17" height="11" fill="#fff"/><path d="M1 1l8 6 8-6" fill="none" stroke="#7fc72a" stroke-width="1.3"/></svg>info@lanternbayfoods.com</span>
    </div>
  </header>

  <section class="abs hero">
    <div role="img" aria-label="Hero photo of steamed dumplings with scallions and red pepper on a dark plate" style="position:absolute;inset:0"></div>
    <div class="brand"><span class="mark"></span>Lantern Bay Foods</div>
    <nav class="nav">
      <a class="active" style="left:0">HOME</a>
      <a style="left:110px">ABOUT US</a>
      <a style="left:246px">PRODUCTS</a>
      <a style="left:389px">CONTACT US</a>
    </nav>
    <svg class="search" width="15" height="15" viewBox="0 0 15 15"><circle cx="6" cy="6" r="4.5" fill="none" stroke="#fff" stroke-width="2"/><path d="M9.5 9.5L14 14" stroke="#fff" stroke-width="2.2"/></svg>
    <span class="arrow" style="left:0;top:281px;border-radius:0 50% 50% 0"><svg width="12" height="14" viewBox="0 0 12 14"><path d="M9 1L3 7l6 6" fill="none" stroke="#222" stroke-width="3"/></svg></span>
    <span class="arrow" style="left:986px;top:281px;border-radius:50% 0 0 50%"><svg width="12" height="14" viewBox="0 0 12 14"><path d="M3 1l6 6-6 6" fill="none" stroke="#222" stroke-width="3"/></svg></span>
    <h1>OUR MISSION IS TO PROVIDE</h1>
    <p>MOST CLEAN, DELICIOUS, AND CONVENIENT FOODS TO OUR CUSTOMERS</p>
  </section>
  <div class="abs green-rule"></div>

  <section class="abs about">
    <h2 class="section-title" style="top:40px">ABOUT <em>LANTERN BAY FOODS</em></h2>
    <div class="divider" style="left:303px;width:428px;top:101px"><i></i></div>
    <p class="copy">Inspired by the name of a famous trade route that connected East Asia and Western countries, Lantern Bay Foods was created to bring traditional and exceptional Asian cuisine to the markets around the globe. LBF's mission is to provide most clean, delicious, and convenient foods to our customers and is committed to promoting healthier lifestyle and sustainability.</p>
    <span class="btn">Read More</span>
  </section>

  <section class="abs products">
    <h2 class="section-title" style="top:43px">PRODUCT</h2>
    <div class="divider" style="left:426px;width:168px;top:88px"><i></i></div>
    <div class="product-photo" role="img" aria-label="Close-up photo of kimchi and pork dumplings, one bitten open, with chopsticks"></div>
    <div class="product-panel">
      <h3>KIMCHI DUMPLINGS</h3>
      <p class="lead">What makes Kimchi &amp; Pork Dumplings so special?</p>
      <h4 style="top:158px"><svg width="18" height="14" viewBox="0 0 18 14"><path d="M1 6h10l-2-4M1 6v7h9l3-3V6" fill="none" stroke="#222" stroke-width="1.5"/></svg><span style="color:#222">HISTORY AND EXCEPTIONAL FLAVOR OF KIMCHI</span></h4>
      <p class="text" style="top:196px">Kimchi, a reddish fermented cabbage mixed with variety of spices like garlic and ginger, was originally developed...[+]</p>
      <h4 style="top:280px"><svg width="18" height="14" viewBox="0 0 18 14"><path d="M1 6h10l-2-4M1 6v7h9l3-3V6" fill="none" stroke="#222" stroke-width="1.5"/></svg><span style="color:#222">HOW BIG IS THIS DUMPLING?</span></h4>
      <p class="text" style="top:316px">Weighing in at around 70 grams per piece, Kimchi &amp; Pork LARGE size dumplings will be the BIGGEST dumpling...[+]</p>
      <span class="btn">Read More</span>
    </div>
    <span class="arrow" style="left:-6px;top:397px"><svg width="10" height="12" viewBox="0 0 10 12"><path d="M8 1L3 6l5 5" fill="none" stroke="#666" stroke-width="2.5"/></svg></span>
    <span class="arrow" style="left:992px;top:397px"><svg width="10" height="12" viewBox="0 0 10 12"><path d="M2 1l5 5-5 5" fill="none" stroke="#666" stroke-width="2.5"/></svg></span>
  </section>

  <section class="abs testimonials">
    <h2 class="section-title" style="top:45px">CLIENT <em>TESTIMONIALS</em></h2>
    <div class="divider" style="left:327px;width:368px;top:87px"><i></i></div>
    <p class="quote">"Lorem ipsum dolor sit amet, consectetuer adipiscing elit, sed diam nonummy nibh euismod tincidunt ut laoreet dolore magna aliquam erat volutpat. Ut wisi enim ad minim veniam, quis nostrud exerci tation ullamcorper suscipit."</p>
    <div class="client-name">
      <svg width="34" height="20" viewBox="0 0 34 20"><circle cx="8" cy="9" r="7" fill="#999"/><circle cx="24" cy="9" r="7" fill="#999"/></svg>
      Maren
      <svg width="34" height="20" viewBox="0 0 34 20"><circle cx="10" cy="11" r="7" fill="#999"/><circle cx="26" cy="11" r="7" fill="#999"/></svg>
    </div>
    <div class="avatar" role="img" aria-label="Client portrait" style="left:364px;top:281px;width:70px;height:70px"></div>
    <div class="avatar current" role="img" aria-label="Client portrait, selected" style="left:464px;top:270px;width:92px;height:92px"></div>
    <div class="avatar" role="img" aria-label="Client portrait" style="left:586px;top:281px;width:70px;height:70px"></div>
  </section>

  <section class="abs newsletter">
    <span class="icon"><svg width="18" height="12" viewBox="0 0 18 12"><rect x="0.5" y="0.5" width="17" height="11" fill="#fff"/><path d="M1 1l8 6 8-6" fill="none" stroke="#222" stroke-width="1.3"/></svg></span>
    <h2>Newsletter Signup</h2>
    <svg class="abs" style="left:345px;top:32px" width="24" height="46" viewBox="0 0 24 46"><path d="M2 2l20 21L2 44" fill="none" stroke="#fff" stroke-width="2"/></svg>
    <div class="field">Enter your email</div>
    <span class="btn">SUBSCRIBE</span>
  </section>

  <footer class="abs footer">
    <h5 style="left:8px">Quick Links</h5>
    <ul>
      <li>› <span>Home</span></li>
      <li>› <span>About Us</span></li>
      <li>› <span>Products</span></li>
      <li>› <span>Contact Us</span></li>
    </ul>
    <h5 style="left:187px">Contact Detail</h5>
    <div class="line" style="top:72px"><svg width="12" height="17" viewBox="0 0 12 17"><path d="M6 16C2 10 1 8 1 6a5 5 0 0110 0c0 2-1 4-5 10z" fill="#fff"/><circle cx="6" cy="6" r="2" fill="#333"/></svg><span>418 Harbor Rd.<br>Cedar Point, CA 90471</span></div>
    <div class="line" style="top:129px"><svg width="14" height="14" viewBox="0 0 14 14"><path d="M2 1l3 3-1.5 1.5c.9 2 2.2 3.3 4 4L9 8l3 3-2 2C6 12.5 1.5 8 1 3z" fill="#fff"/></svg><span>555 010 2468</span></div>
    <div class="line" style="top:169px"><svg width="14" height="14" viewBox="0 0 14 14"><rect x="3" y="1" width="8" height="4" fill="#fff"/><rect x="1" y="5" width="12" height="6" fill="#fff"/><rect x="3" y="9" width="8" height="4" fill="#fff" stroke="#333"/></svg><span>555 010 2468</span></div>
    <div class="line" style="top:209px"><svg width="16" height="11" viewBox="0 0 16 11"><rect x="0.5" y="0.5" width="15" height="10" fill="#fff"/><path d="M1 1l7 5 7-5" fill="none" stroke="#333"/></svg><span>info@lanternbayfoods.com</span></div>
    <h5 style="left:492px">Map</h5>
    <div class="map" role="img" aria-label="Street map showing the company location"></div>
    <div class="footer-brand"><span class="mark"></span>Lantern Bay Foods</div>
  </footer>

  <div class="abs bottom">
    <p>Copyright © 2016 Lantern Bay Foods.  All Rights Reserved</p>
    <span class="social" style="left:930px"></span>
    <span class="social" style="left:958px"></span>
    <span class="social" style="left:986px"></span>
  </div>

</div>
</body>
</html>
```